Business Card Design Project

I am a property development company requiring a professional looking business card.
The name of the my company is PLW CANOPIES. I have attached a couple of designs that I have created on my own, that can give you an idea of what I am after.
Above the wording PLW CANOPIES, I have a orange arc above these words to signify the sun is begining to rise above the horizon.
I have a few designs; Middle Rays, Side Rays, Horizontals Rays which are OK, but I am looking for the better design.
The Rear design of the card is what I had came up with. If you have a better design, I am happy to see it.
The design of the card can follow what I have came up with, or it can be totally different. The fonts needs to be adjusted to another font that is more suitable.
The colours that I have used is what I think I would like to stick with. As I have mentioned, the orange arc is to signify the sun rising. If you have a better colour scheme, I would consider it.
Looking at dealing with first home buyers and proffesional people.
Business

```html
<!DOCTYPE html>
<html lang="en">
<head>
<meta charset="utf-8">
<title>PLW Canopies – Business Card</title>
<link rel="stylesheet" href="https://fonts.googleapis.com/css2?family=Alfa+Slab+One&family=Arimo:wght@400&family=Kaushan+Script&display=swap">
<style>
  :root {
    --paper: #ffffff;
    --ink: #2b2b2b;
    --ink-soft: #333333;
    --red: #e5232b;
    --orange: #f5821f;
    --yellow: #fdc82f;
    --pale-yellow: #fde9a6;
    --emblem: #f08a4b;
    --edge: #6b6b6b;
  }
  * { box-sizing: border-box; margin: 0; padding: 0; }
  html, body {
    width: 1200px; height: 694px; overflow: hidden;
    background: var(--paper);
  }
  .sheet { position: relative; width: 1200px; height: 694px; }
  .card {
    position: absolute;
    width: 576px; height: 312px;
    background: var(--paper);
    border: 1px solid var(--edge);
    box-shadow: 2px 2px 2px rgba(0,0,0,.35);
    overflow: hidden;
  }
  .card--a { left: 2px;   top: 20px; }
  .card--b { left: 621px; top: 20px; }
  .card--c { left: 2px;   top: 364px; }
  .card--d { left: 621px; top: 376px; }
  .card__bands { position: absolute; inset: 0; width: 100%; height: 100%; }
  .card__address, .card__online {
    position: absolute; top: 6px;
    font-family: "Arimo", Arial, sans-serif;
    font-size: 17px; line-height: 18px; color: var(--ink);
  }
  .card__address { left: 8px; }
  .card__online { right: 8px; text-align: right; }
  .card__emblem {
    position: absolute; left: 276px; top: 98px;
    width: 24px; height: 24px; border-radius: 50%;
    background: var(--emblem);
  }
  .card__name {
    position: absolute; left: 0; width: 576px; top: 128px;
    text-align: center; padding-right: 20px;
    font-family: "Kaushan Script", cursive;
    font-size: 37px; line-height: 40px; color: var(--ink);
  }
  .card__role {
    position: absolute; left: 0; width: 576px; top: 164px;
    text-align: center; padding-right: 30px;
    font-family: "Alfa Slab One", serif;
    font-size: 28px; line-height: 34px; letter-spacing: 1px; color: var(--ink);
  }
  .card__company {
    position: absolute; right: 8px; bottom: 8px;
    text-align: right; color: var(--ink-soft);
    font-family: "Alfa Slab One", serif;
  }
  .card__company-name { font-size: 33px; line-height: 34px; letter-spacing: 1px; }
  .card__company-line { font-size: 19px; line-height: 22px; }
</style>
</head>
<body>
<main class="sheet">
  <svg width="0" height="0" style="position:absolute" aria-hidden="true">
    <defs>
      <linearGradient id="top-band" x1="0" y1="0" x2="0.6" y2="0.7">
        <stop offset="0" stop-color="var(--red)"/>
        <stop offset="0.35" stop-color="var(--orange)"/>
        <stop offset="0.75" stop-color="var(--yellow)"/>
      </linearGradient>
      <linearGradient id="bottom-band" x1="0" y1="1" x2="0.5" y2="0.2">
        <stop offset="0" stop-color="var(--red)"/>
        <stop offset="0.3" stop-color="var(--orange)"/>
        <stop offset="0.7" stop-color="var(--yellow)"/>
      </linearGradient>
      <symbol id="card-bands" viewBox="0 0 576 312">
        <path d="M0,0 H576 V70 C430,82 260,100 150,135 C80,156 30,172 0,185 Z" fill="var(--pale-yellow)"/>
        <path d="M0,0 H576 V52 C430,58 260,80 140,115 C70,136 25,150 0,162 Z" fill="url(#top-band)"/>
        <path d="M0,312 V268 C160,255 320,222 576,196 V312 Z" fill="var(--pale-yellow)"/>
        <path d="M0,312 V290 C160,276 330,238 576,214 V312 Z" fill="url(#bottom-band)"/>
      </symbol>
    </defs>
  </svg>

  <article class="card card--a">
    <svg class="card__bands" viewBox="0 0 576 312" preserveAspectRatio="none" aria-hidden="true"><use href="#card-bands"/></svg>
    <p class="card__address">27 Harbour St Kelso<br>N.S.W. Australia 2795<br>Mob: 0412 555 019</p>
    <p class="card__online">Email: marcus@plwcanopies.com<br>Web: www.plwcanopies.com</p>
    <div class="card__emblem" role="img" aria-label="PLW Canopies emblem"></div>
    <p class="card__name">Marcus Reid</p>
    <p class="card__role">DIRECTOR</p>
    <div class="card__company"><p class="card__company-name">PLW CANOPIES</p><p class="card__company-line">PROPERTY DEVELOPMENTS</p></div>
  </article>

  <article class="card card--b">
    <svg class="card__bands" viewBox="0 0 576 312" preserveAspectRatio="none" aria-hidden="true"><use href="#card-bands"/></svg>
    <p class="card__address">27 Harbour St Kelso<br>N.S.W. Australia 2795<br>Mob: 0412 555 019</p>
    <p class="card__online">Email: marcus@plwcanopies.com<br>Web: www.plwcanopies.com</p>
    <div class="card__emblem" role="img" aria-label="PLW Canopies emblem"></div>
    <p class="card__name">Marcus Reid</p>
    <p class="card__role">DIRECTOR</p>
    <div class="card__company"><p class="card__company-name">PLW CANOPIES</p><p class="card__company-line">PROPERTY DEVELOPMENTS</p></div>
  </article>

  <article class="card card--c">
    <svg class="card__bands" viewBox="0 0 576 312" preserveAspectRatio="none" aria-hidden="true"><use href="#card-bands"/></svg>
    <p class="card__address">27 Harbour St Kelso<br>N.S.W. Australia 2795<br>Mob: 0412 555 019</p>
    <p class="card__online">Email: marcus@plwcanopies.com<br>Web: www.plwcanopies.com</p>
    <div class="card__emblem" role="img" aria-label="PLW Canopies emblem"></div>
    <p class="card__name">Marcus Reid</p>
    <p class="card__role">DIRECTOR</p>
    <div class="card__company"><p class="card__company-name">PLW CANOPIES</p><p class="card__company-line">PROPERTY DEVELOPMENTS</p></div>
  </article>

  <article class="card card--d">
    <svg class="card__bands" viewBox="0 0 576 312" preserveAspectRatio="none" aria-hidden="true"><use href="#card-bands"/></svg>
    <p class="card__address">27 Harbour St Kelso<br>N.S.W. Australia 2795<br>Mob: 0412 555 019</p>
    <p class="card__online">Email: marcus@plwcanopies.com<br>Web: www.plwcanopies.com</p>
    <div class="card__emblem" role="img" aria-label="PLW Canopies emblem"></div>
    <p class="card__name">Marcus Reid</p>
    <p class="card__role">DIRECTOR</p>
    <div class="card__company"><p class="card__company-name">PLW CANOPIES</p><p class="card__company-line">PROPERTY DEVELOPMENTS</p></div>
  </article>
</main>
</body>
</html>
```